Need web design for our e-assessment company

We need a web design for our e-assessment company called Tavelo. We develop modern, web-based software for supporting the testing and examination process. The application is delivered as a SaaS solution.

The application helps our customers save time and money.

The design should communicate the following:

- Modern
- Innovation
- Security
- Performance

Attached you can find a screenshot of our application as well as some thoughts on the website.

We would like a front page as well as 1 sub page.

And lastly, one more website we draw inspiration from (on top of the ones mentioned in the attached document): http://www.plonkavery.example/
Updates

Dear all,

I have updated the description with 1 more example of websites we like as well as added that we would like a front page and a sub page.

Thanks in advance.

Best regards,

Torlak

Target Market(s)

Our target groups are higher education and awarding organisations. Decision makers are mostly men age 45+.

Industry/Entity Type

It Company

Requirements
Must have
• 1 front page and 1 sub page

```html
<!DOCTYPE html>
<html lang="en">
<head>
<meta charset="utf-8">
<title>Tavelo – e-Assessment made simple</title>
<link rel="stylesheet" href="https://fonts.googleapis.com/css2?family=Raleway:wght@400;500;600;700;800&display=swap">
<style>
:root{
  --orange:#f26a1b;
  --orange-dark:#d9560c;
  --band-orange:#e77b33;
  --blue:#1aa0e6;
  --blue-btn:#3aa6e8;
  --ink:#4a4e58;
  --ink-soft:#8a8f9a;
  --ink-light:#a3a8b2;
  --line:#e3e6ea;
  --bg:#fafbfc;
  --cta-bg:#dde0e8;
  --partner:#c3c7cd;
}
*{box-sizing:border-box;margin:0;padding:0}
html,body{width:1024px;height:1200px;overflow:hidden}
body{position:relative;background:var(--bg);font-family:"Raleway",sans-serif;color:var(--ink)}
.abs{position:absolute}

/* top bar */
.topbar{left:0;top:0;width:1024px;height:32px;background:#fff;border-bottom:1px solid var(--line)}
.topbar .sep{top:0;width:1px;height:32px;background:var(--line)}
.sq{top:7px;width:19px;height:19px;background:#c9ccd2}
.contact{top:10px;font-size:10px;color:var(--ink-soft);display:flex;align-items:center;gap:6px}

/* header */
.header{left:0;top:33px;width:1024px;height:68px;background:#fff;border-bottom:1px solid var(--line)}
.brand-dot{left:144px;top:6px;width:52px;height:52px;border-radius:50%;background:var(--orange)}
.brand-name{left:206px;top:9px;font-size:40px;font-weight:500;color:#5a5e66;letter-spacing:-1px}
.nav a{position:absolute;top:26px;font-size:10.5px;color:#5f636b;text-decoration:none}
.nav a.active{color:var(--blue);font-weight:700}
.btn{position:absolute;display:flex;align-items:center;justify-content:center;color:#fff;font-weight:700;border-radius:3px;text-decoration:none}
.btn-orange{background:linear-gradient(#fb8a3c,var(--orange-dark));border:1px solid #e0601a}
.btn-blue{background:linear-gradient(#5dbaf0,#2f95dc);border:1px solid #2a8ed4}

/* hero */
.hero{left:0;top:102px;width:1024px;height:332px;background:linear-gradient(180deg,#eef0f4 0%,#f6f7f9 55%,#e4e6ec 100%)}
.hero h1{position:absolute;left:132px;top:88px;font-size:29px;font-weight:700;color:#4c4f57;letter-spacing:-.3px}
.hero h1 span{color:var(--orange)}
.hero p{position:absolute;left:133px;top:135px;width:420px;font-size:13.5px;line-height:20px;color:#7b7f88}
.hero-photo{left:520px;top:0;width:380px;height:332px;background:radial-gradient(ellipse at 60% 40%,#e6d4c6 0%,#e9e4e0 45%,rgba(238,240,244,0) 75%)}

/* feature band */
.features{left:0;top:434px;width:1024px;height:145px;background:linear-gradient(180deg,#eb8b4c,var(--band-orange))}
.features .div{top:0;width:1px;height:145px;background:rgba(255,255,255,.25)}
.feature{position:absolute;top:0;height:145px;text-align:center;color:#fff}
.feature h3{position:absolute;left:0;right:0;top:89px;font-size:13px;font-weight:700}
.feature p{position:absolute;left:0;right:0;top:110px;font-size:9.5px;text-transform:uppercase;color:rgba(255,255,255,.85)}
.feature svg{position:absolute;left:50%;transform:translateX(-50%);top:22px}

/* video */
.player{left:136px;top:618px;width:369px;height:184px;background:#3b3f47;border-radius:3px;overflow:hidden}
.player .screen{left:0;top:0;width:369px;height:152px;background:linear-gradient(90deg,#2a2e36 0 43px,#d9dbde 43px)}
.player .controls{left:0;top:152px;width:369px;height:32px;background:#1c1e22}
.player .track{left:98px;top:15px;width:160px;height:3px;background:#555}
.player .track span{display:block;width:57px;height:3px;background:#e5495b}
.player .time{left:271px;top:10px;font-size:8px;color:#ddd}
.intro h2{position:absolute;left:522px;top:618px;width:360px;font-size:23px;font-weight:500;line-height:29px;color:#4a4d55}
.intro h2 span{color:var(--orange)}
.intro p{position:absolute;left:524px;top:690px;width:370px;font-size:10px;line-height:14.5px;color:var(--ink-soft)}
.checks{position:absolute;left:523px;top:737px;list-style:none}
.checks li{height:25.5px;font-size:10px;color:var(--ink-soft);display:flex;align-items:center;gap:6px}

/* columns */
.col-title{position:absolute;top:858px;font-size:22px;font-weight:500;color:#52555d}
.case h4{position:absolute;left:138px;top:903px;font-size:11px;font-weight:700;color:var(--blue)}
.case p{position:absolute;left:138px;width:220px;font-size:10px;line-height:16px;color:var(--ink-soft)}
.news-thumb{left:394px;width:43px;height:43px;background:linear-gradient(135deg,#8a8f98,#3e424a)}
.news-text{position:absolute;left:448px;width:180px;font-size:10px;line-height:16px;color:var(--ink-soft)}
.news-text time{display:block;color:#5a5e66;font-size:9.5px}
.partner{background:var(--partner)}

/* cta */
.cta{left:0;top:1065px;width:1024px;height:89px;background:var(--cta-bg);overflow:hidden}
.cta .c{position:absolute;border-radius:50%;background:rgba(190,194,204,.55)}
.cta h2{position:absolute;left:273px;top:31px;font-size:22.5px;font-weight:700;color:#6b7080}
.cta h2 span{color:var(--blue)}

/* footer */
.footer{left:0;top:1154px;width:1024px;height:46px;background:#fff}
.footer .copy{position:absolute;left:138px;top:19px;font-size:10.5px;color:#b7bbc3}
.circ{position:absolute;top:17px;width:18px;height:18px;border-radius:50%;background:#c4c7cd}
</style>
</head>
<body>

<div class="abs topbar">
  <div class="abs sep" style="left:510px"></div>
  <div class="abs sq" style="left:522px"></div>
  <div class="abs sq" style="left:552px"></div>
  <div class="abs sq" style="left:582px"></div>
  <div class="abs sq" style="left:612px"></div>
  <div class="abs sep" style="left:640px"></div>
  <div class="abs contact" style="left:653px">
    <svg width="24" height="12" viewBox="0 0 24 12"><path d="M0 3h5M2 6h5M4 9h4" stroke="#9aa3b0"/><rect x="9" y="1" width="14" height="10" fill="none" stroke="#4a90d9"/><path d="M9 1l7 6 7-6" fill="none" stroke="#4a90d9"/></svg>
    hello@tavelo.example
  </div>
  <div class="abs sep" style="left:775px"></div>
  <div class="abs contact" style="left:787px">
    <svg width="12" height="12" viewBox="0 0 12 12"><path d="M3 1l2 2.5-1.2 1.5c.6 1.4 1.7 2.5 3.2 3.2L8.5 7 11 9l-1.5 2C5 11 1 7 1 2.5z" fill="none" stroke="#4a90d9"/></svg>
    +00 555 204 871
  </div>
</div>

<header class="abs header">
  <div class="abs brand-dot"></div>
  <div class="abs brand-name">tavelo</div>
  <nav class="nav">
    <a class="active" href="#" style="left:376px">Home</a>
    <a href="#" style="left:442px">Solutions</a>
    <a href="#" style="left:517px">Features</a>
    <a href="#" style="left:589px">Blog</a>
    <a href="#" style="left:642px">About</a>
    <a href="#" style="left:704px">Contact</a>
  </nav>
  <a class="btn btn-orange" href="#" style="left:771px;top:15px;width:112px;height:36px;font-size:13.5px">Get FREE Trial</a>
</header>

<section class="abs hero">
  <div class="abs hero-photo" role="img" aria-label="Smiling woman in a white blazer leaning beside an open laptop showing the assessment dashboard"></div>
  <h1>e-Assessment made <span>simple</span>.</h1>
  <p>Lorem ipsum dolor sit amet, consectetur adipisicing elit, sed do eiusmod tempor incididunt ut labore et dolore magna aliqua.</p>
  <a class="btn btn-blue" href="#" style="left:135px;top:209px;width:88px;height:31px;font-size:10.5px">View Pricing</a>
  <a class="btn btn-orange" href="#" style="left:230px;top:209px;width:88px;height:31px;font-size:10.5px">Get FREE Trial</a>
</section>

<section class="abs features">
  <div class="abs div" style="left:384px"></div>
  <div class="abs div" style="left:641px"></div>
  <div class="feature" style="left:0;width:384px">
    <svg width="58" height="56" viewBox="0 0 58 56"><g fill="#fff"><rect y="0" width="58" height="16" rx="2"/><rect y="20" width="58" height="16" rx="2"/><rect y="40" width="58" height="16" rx="2"/></g><g fill="var(--band-orange)"><rect x="6" y="6" width="38" height="4"/><rect x="6" y="26" width="38" height="4"/><rect x="6" y="46" width="38" height="4"/><circle cx="51" cy="8" r="2.5"/><circle cx="51" cy="28" r="2.5"/><circle cx="51" cy="48" r="2.5"/></g></svg>
    <h3 style="top:87px">No Servers</h3><p style="top:108px">Lorem ipsum dolor sit amet</p>
  </div>
  <div class="feature" style="left:385px;width:256px">
    <svg width="76" height="60" viewBox="0 0 76 60"><g fill="#fff"><circle cx="26" cy="36" r="17"/><g stroke="#fff" stroke-width="8"><path d="M26 12v48M2 36h48M9 19l34 34M43 19L9 53"/></g><circle cx="58" cy="14" r="10"/><g stroke="#fff" stroke-width="5"><path d="M58 0v28M44 14h28M48 4l20 20M68 4L48 24"/></g></g><circle cx="26" cy="36" r="7" fill="var(--band-orange)"/><circle cx="58" cy="14" r="4" fill="var(--band-orange)"/></svg>
    <h3>No Maintenance</h3><p>Lorem ipsum dolor sit amet</p>
  </div>
  <div class="feature" style="left:642px;width:382px">
    <svg width="60" height="56" viewBox="0 0 60 56"><g fill="#fff"><rect x="0" y="26" width="12" height="28"/><path d="M16 26l10-12 6-14c5 0 7 4 6 9l-3 11h18c5 0 7 4 6 7l-2 4c2 2 2 5 0 7 1 3 0 5-2 6 0 4-2 6-6 6H16z"/></g></svg>
    <h3>No Worries</h3><p>Lorem ipsum dolor sit amet</p>
  </div>
</section>

<div class="abs player">
  <div class="abs screen" role="img" aria-label="Video still of the Tavelo dashboard with collections, assessments, tasks and a percentage report chart"></div>
  <svg class="abs" style="left:188px;top:57px" width="54" height="54" viewBox="0 0 54 54"><circle cx="27" cy="27" r="25" fill="rgba(255,255,255,.35)" stroke="#fff" stroke-width="4"/><circle cx="27" cy="27" r="17" fill="#fff"/><path d="M22 19l13 8-13 8z" fill="#777"/></svg>
  <div class="abs controls">
    <svg class="abs" style="left:18px;top:9px" width="14" height="14" viewBox="0 0 14 14"><circle cx="7" cy="7" r="6" fill="none" stroke="#fff" stroke-width="1.5"/><path d="M5.5 4.5l4 2.5-4 2.5z" fill="#fff"/></svg>
    <svg class="abs" style="left:44px;top:10px" width="45" height="12" viewBox="0 0 45 12"><path d="M0 4h3l4-3v10L3 8H0z" fill="#e5495b"/><path d="M9 3q2 3 0 6" stroke="#e5495b" fill="none"/><g fill="#ddd"><rect x="16" y="2" width="2" height="8"/><rect x="20" y="2" width="2" height="8"/><rect x="24" y="2" width="2" height="8"/><rect x="28" y="2" width="2" height="8"/><rect x="32" y="2" width="2" height="8"/></g><g fill="#777"><rect x="36" y="2" width="2" height="8"/><rect x="40" y="2" width="2" height="8"/></g></svg>
    <div class="abs track"><span></span></div>
    <div class="abs time">01:30 / 04:55</div>
    <svg class="abs" style="left:330px;top:11px" width="11" height="9"><rect x="1" y="1" width="9" height="7" fill="none" stroke="#fff" stroke-width="1.5"/></svg>
    <svg class="abs" style="left:351px;top:10px" width="11" height="11" viewBox="0 0 11 11"><circle cx="5.5" cy="5.5" r="3.5" fill="none" stroke="#fff" stroke-width="2.5" stroke-dasharray="2 1.4"/><circle cx="5.5" cy="5.5" r="1.2" fill="#fff"/></svg>
  </div>
</div>

<div class="intro">
  <h2>Making assessments <span>simple and easy</span> for everyone.</h2>
  <p>Lorem ipsum dolor sit amet, consectetur adipisicing elit, sed do eiusmod tempor incididunt ut labore et dolore magna aliqua. Ut enim ad minim veniam, quis</p>
  <ul class="checks">
    <li><svg width="9" height="8"><path d="M1 4l2.5 2.5L8 1" stroke="#9aa0aa" stroke-width="2" fill="none"/></svg>Lower long-term costs</li>
    <li><svg width="9" height="8"><path d="M1 4l2.5 2.5L8 1" stroke="#9aa0aa" stroke-width="2" fill="none"/></svg>Instant feedback to students</li>
    <li><svg width="9" height="8"><path d="M1 4l2.5 2.5L8 1" stroke="#9aa0aa" stroke-width="2" fill="none"/></svg>Greater flexibility with respect to location and timing</li>
  </ul>
</div>

<h2 class="col-title" style="left:136px">Case Studies</h2>
<h2 class="col-title" style="left:393px">Latest News</h2>
<h2 class="col-title" style="left:648px">Our Partners</h2>

<div class="case">
  <h4>CASE STUDY HEADLINE</h4>
  <p style="top:925px">Donec quis facilisis libero. Donec eget ornare tortor. Proin gravida, lectus nec fermentum bibendum.</p>
  <p style="top:989px">Nullam interdum vehicula urna ut laoreet.ulla eleifend suscipit fringilla. Morbi mollis ut lorem</p>
</div>

<div class="abs news-thumb" style="top:906px" role="img" aria-label="Two business people in an office"></div>
<div class="news-text" style="top:902px">Nunc purus orci, adipiscing non ipsum non, pellentesque fringilla sapien.<time>October 15, 2013</time></div>
<div class="abs news-thumb" style="top:979px" role="img" aria-label="Student concentrating on her work"></div>
<div class="news-text" style="top:975px">Nunc purus orci, adipiscing non ipsum non, pellentesque fringilla sapien.<time>October 15, 2013</time></div>

<div class="abs partner" style="left:652px;top:912px;width:94px;height:42px;border-radius:4px"></div>
<div class="abs partner" style="left:788px;top:908px;width:76px;height:48px;border-radius:24px"></div>
<div class="abs partner" style="left:652px;top:984px;width:100px;height:32px;border-radius:4px"></div>
<div class="abs partner" style="left:792px;top:978px;width:70px;height:46px;border-radius:50%"></div>

<section class="abs cta">
  <div class="c" style="left:135px;top:-25px;width:110px;height:110px"></div>
  <div class="c" style="left:71px;top:38px;width:62px;height:62px"></div>
  <div class="c" style="left:236px;top:44px;width:38px;height:38px"></div>
  <div class="c" style="left:926px;top:-20px;width:118px;height:118px"></div>
  <div class="c" style="left:856px;top:40px;width:70px;height:70px"></div>
  <div class="c" style="left:985px;top:60px;width:40px;height:40px"></div>
  <h2>Start using Tavelo now for <span>FREE</span> 30-days trial!</h2>
  <a class="btn btn-orange" href="#" style="left:779px;top:27px;width:112px;height:36px;font-size:12.5px">Get FREE Trial</a>
</section>

<footer class="abs footer">
  <div class="copy">Copyright © 2014 - Tavelo.example</div>
  <span class="circ" style="left:545px"></span>
  <span class="circ" style="left:573px"></span>
  <span class="circ" style="left:601px"></span>
  <span class="circ" style="left:629px"></span>
  <div class="abs contact" style="left:673px;top:19px;font-size:9.5px">
    <svg width="24" height="12" viewBox="0 0 24 12"><path d="M0 3h5M2 6h5M4 9h4" stroke="#9aa3b0"/><rect x="9" y="1" width="14" height="10" fill="none" stroke="#4a90d9"/><path d="M9 1l7 6 7-6" fill="none" stroke="#4a90d9"/></svg>
    hello@tavelo.example
  </div>
  <div class="abs contact" style="left:800px;top:19px;font-size:9.5px">
    <svg width="12" height="12" viewBox="0 0 12 12"><path d="M3 1l2 2.5-1.2 1.5c.6 1.4 1.7 2.5 3.2 3.2L8.5 7 11 9l-1.5 2C5 11 1 7 1 2.5z" fill="none" stroke="#4a90d9"/></svg>
    +00 555 204 871
  </div>
</footer>

</body>
</html>
```